New concept for existing event brand

I have this current brand - www.velltrix-quarter.com I have attached an example of a credible event on 23rd December and then a more fun brunch event.

I require a new flyer for a new concept - Fernwick Frolics - (there is no logo yet) it is at a venue which has ball pits, table tennis, beer pong, arcades etc

I am looking for an artwork which portrays a fun event but also retains the cooler brand identify

One idea was having the images in polaroid frames

Fernwick Frolics

Saturday 18th February 2023

Venue to be announced • 3pm-9pm

2 giant ball pits
Beer pong
Ping Pong
Boxing machines
Dance Machine
Air Hockey
Pool
Giant board games
Giant Stackle 6
Photo Booth
Spin The Wheel
Table Football
Retro Arcade Games
Pinball

Food
Pizzas
Brimsy Bowls
Popcorn
Candy Floss

Cocktails
Alcoholic Chillo Kittens
Beer Towers
Spirits & Mixers

```html
<!DOCTYPE html>
<html lang="en">
<head>
<meta charset="utf-8">
<title>Fernwick Frolics – Flyer</title>
<link rel="stylesheet" href="https://fonts.googleapis.com/css2?family=Montserrat:wght@400;500;700;800;900&family=Allura&display=swap">
<style>
  :root {
    --ink: #0b0b0c;
    --charcoal: #1d1d20;
    --pink: #e8128f;
    --pink-light: #f24bb0;
    --green: #3bb56a;
    --green-text: #2fae5e;
    --white: #ffffff;
    --paper: #f6f6f6;
    --grey-faint: #2c2c30;
    --rule: #8a8a8e;
  }
  * { box-sizing: border-box; margin: 0; padding: 0; }
  html, body { width: 815px; height: 1200px; overflow: hidden; background: var(--ink); }
  .flyer {
    position: relative; width: 815px; height: 1200px; overflow: hidden;
    font-family: "Montserrat", sans-serif; color: var(--white);
    background:
      radial-gradient(ellipse 70% 18% at 50% 60%, #26262a 0%, transparent 70%),
      linear-gradient(180deg, #151517 0%, #0a0a0b 35%, #1a1a1c 58%, #060607 80%, #0a0a0b 100%);
  }
  .brand {
    position: absolute; top: 44px; left: 0; width: 100%; text-align: center;
    font-weight: 900; font-size: 46px; letter-spacing: -1px; color: #d9d9dc;
  }
  .polaroid {
    position: absolute; background: var(--paper); padding: 10px;
    box-shadow: 0 6px 14px rgba(0,0,0,.7);
  }
  .polaroid .photo { width: 100%; height: 100%; }
  .polaroid--top { top: 136px; width: 228px; height: 256px; }
  .polaroid--one { left: 56px; }
  .polaroid--two { left: 298px; }
  .polaroid--three { left: 540px; }
  .photo--mural { background: linear-gradient(160deg, #7a5bd0 0%, #3a2a6e 45%, #d9b8e6 100%); }
  .photo--pong { background: linear-gradient(170deg, #3b3f8c 0%, #5a4fa0 50%, #c8233a 100%); }
  .photo--balls { background: radial-gradient(circle at 50% 40%, #2a1a3a 0%, #b58be0 45%, #efe3f7 100%); }
  .title-main {
    position: absolute; top: 410px; left: 0; width: 100%; text-align: center;
    font-weight: 900; font-size: 104px; letter-spacing: -3px; line-height: 1;
    color: var(--pink); text-shadow: 0 0 0 #000, 5px 5px 0 #000, -2px -2px 0 #000, 2px -2px 0 #000, -2px 2px 0 #000;
  }
  .title-script {
    position: absolute; top: 520px; left: 0; width: 100%; text-align: center;
    font-family: "Allura", cursive; font-size: 92px; line-height: 1; color: var(--white);
  }
  .frame { position: absolute; left: 56px; top: 583px; width: 711px; height: 400px; }
  .date-band {
    position: absolute; left: 101px; top: 644px; width: 614px; height: 56px;
    background: var(--green); color: var(--ink); text-align: center;
    font-weight: 800; font-size: 31px; letter-spacing: 3px; line-height: 56px;
  }
  .year {
    position: absolute; left: 440px; top: 696px; width: 260px; text-align: center;
    font-weight: 900; font-size: 84px; line-height: 1; color: var(--green-text);
    text-shadow: 3px 3px 0 #000;
  }
  .details { position: absolute; left: 138px; top: 716px; font-size: 24px; font-weight: 500; line-height: 30px; }
  .details-echo {
    position: absolute; left: 206px; top: 750px; font-size: 36px; font-weight: 800;
    color: var(--grey-faint); letter-spacing: 2px;
  }
  .activities {
    position: absolute; top: 818px; left: 0; width: 100%; text-align: center;
    font-size: 20px; line-height: 30px; color: #e8e8ea; list-style: none;
  }
  .activities .sep { color: var(--pink); padding: 0 3px; }
  .contact-band {
    position: absolute; left: 39px; top: 1004px; width: 736px; height: 138px; background: var(--pink);
  }
  .menu-card {
    position: absolute; top: 974px; width: 148px; height: 192px; background: var(--white);
    padding: 8px; box-shadow: 0 4px 10px rgba(0,0,0,.6);
  }
  .menu-card--food { left: 84px; }
  .menu-card--drinks { left: 250px; }
  .menu-card .photo { height: 78px; }
  .photo--ballpit { background: linear-gradient(160deg, #c81d2c 0%, #e8e4e4 55%, #b81424 100%); }
  .photo--party { background: linear-gradient(160deg, #c9b7a0 0%, #3a2a1e 50%, #d8d2cc 100%); }
  .menu-list { list-style: none; margin-top: 8px; font-size: 11.5px; font-weight: 800; color: var(--ink); line-height: 17px; }
  .menu-list li::before {
    content: ""; display: inline-block; width: 5px; height: 5px; border-radius: 50%;
    background: var(--green); margin: 0 5px 2px 0; vertical-align: middle;
  }
  .menu-list .inline::before { margin-left: 6px; }
  .menu-list--food li { display: inline-block; }
  .menu-list--food .row { display: block; }
  .contact {
    position: absolute; left: 430px; top: 1022px; width: 330px; text-align: center;
  }
  .contact-heading { font-weight: 800; font-size: 24px; display: flex; align-items: center; justify-content: center; gap: 14px; }
  .contact-heading::before, .contact-heading::after { content: ""; width: 40px; height: 2px; background: var(--ink); }
  .contact-site { font-weight: 800; font-size: 23px; margin-top: 10px; }
  .contact-email { font-weight: 400; font-size: 16px; margin-top: 8px; letter-spacing: .3px; }
</style>
</head>
<body>
<main class="flyer">
  <div class="brand">VELLTRIX QUARTER</div>

  <figure class="polaroid polaroid--top polaroid--one"><div class="photo photo--mural" role="img" aria-label="Guest posing by a colourful mural with a giant sunflower"></div></figure>
  <figure class="polaroid polaroid--top polaroid--two"><div class="photo photo--pong" role="img" aria-label="Friends playing beer pong at a red table"></div></figure>
  <figure class="polaroid polaroid--top polaroid--three"><div class="photo photo--balls" role="img" aria-label="Guest jumping into a ball pit under purple light"></div></figure>

  <svg class="frame" viewBox="0 0 711 400" aria-hidden="true">
    <path d="M160 1 H1 V400 M551 1 H710 V400" fill="none" stroke="var(--rule)" stroke-width="1.5"/>
  </svg>

  <h1 class="title-main">FERNWICK</h1>
  <div class="title-script">Frolics</div>

  <div class="date-band">SATURDAY 18TH FEBRUARY</div>
  <div class="details-echo">3PM-9PM</div>
  <div class="year">2023</div>
  <p class="details">Venue to be announced<br>3pm-9pm</p>

  <ul class="activities">
    <li>2 giant ball pits <span class="sep">|</span> Beer pong <span class="sep">|</span> Ping Pong <span class="sep">|</span> Boxing machines</li>
    <li>Dance Machine <span class="sep">|</span> Air Hockey <span class="sep">|</span> Pool <span class="sep">|</span> Giant board games</li>
    <li>Giant Stackle 6 <span class="sep">|</span> Photo Booth <span class="sep">|</span> Spin The Wheel</li>
    <li>Table Football <span class="sep">|</span> Retro Arcade Games <span class="sep">|</span> Pinball</li>
  </ul>

  <div class="contact-band"></div>

  <section class="menu-card menu-card--food">
    <div class="photo photo--ballpit" role="img" aria-label="Guests in a red and white ball pit"></div>
    <ul class="menu-list menu-list--food">
      <li>FOOD</li><li class="inline">PIZZAS</li>
      <li class="row">BRIMSY BOWLS</li>
      <li class="row">POPCORN</li>
      <li class="row">CANDY FLOSS</li>
    </ul>
  </section>

  <section class="menu-card menu-card--drinks">
    <div class="photo photo--party" role="img" aria-label="Smiling guest in a ball pit"></div>
    <ul class="menu-list">
      <li>COCKTAILS</li>
      <li>BEER TOWERS</li>
      <li>SPIRITS &amp; MIXERS</li>
      <li>ALCOHOLIC CHILLO KITTENS</li>
    </ul>
  </section>

  <div class="contact">
    <div class="contact-heading">CONTACT US</div>
    <div class="contact-site">VELLTRIX-QUARTER.COM</div>
    <div class="contact-email">SUPPORT@VELLTRIX-QUARTER.COM</div>
  </div>
</main>
</body>
</html>
```